Maple Ridge business card design

Card needs to include the following text/items:
Company Logo
Tobin Marsh
Phone # - 555-318-7642
service@mapleridgelandscaping.example
Lawn & landscape maintenance services

```html
<!DOCTYPE html>
<html lang="en">
<head>
<meta charset="utf-8">
<title>Maple Ridge Landscaping – Business Card</title>
<link rel="stylesheet" href="https://fonts.googleapis.com/css2?family=Marcellus&family=Roboto:ital,wght@0,400;1,400&display=swap">
<style>
  :root {
    --forest: #022a17;
    --amber: #f7a12a;
    --paper: #ffffff;
    --backdrop: #f4f4f4;
    --leaf: #3d7a3f;
  }
  html, body {
    margin: 0;
    padding: 0;
    width: 800px;
    height: 1200px;
    overflow: hidden;
    background: var(--backdrop);
  }
  .canvas {
    position: relative;
    width: 800px;
    height: 1200px;
  }
  .card {
    position: absolute;
    left: 50px;
    width: 700px;
    height: 400px;
    background: var(--paper);
    overflow: hidden;
    box-shadow: 0 2px 8px rgba(0,0,0,0.18);
  }
  .card--front { top: 150px; }
  .card--back { top: 640px; }
  .card__shapes {
    position: absolute;
    inset: 0;
    width: 700px;
    height: 400px;
  }
  .card__name {
    position: absolute;
    left: 40px;
    top: 56px;
    margin: 0;
    font-family: "Marcellus", serif;
    font-weight: 400;
    font-size: 41px;
    letter-spacing: 0.5px;
    color: var(--forest);
  }
  .card__details {
    position: absolute;
    left: 42px;
    top: 234px;
    font-family: "Roboto", sans-serif;
    color: var(--paper);
  }
  .card__tagline {
    margin: 0 0 8px;
    font-style: italic;
    font-size: 18px;
    line-height: 26px;
    color: var(--amber);
  }
  .contact {
    display: flex;
    align-items: center;
    gap: 10px;
    font-size: 17px;
    line-height: 29px;
  }
  .contact__icon {
    width: 13px;
    height: 13px;
    fill: var(--amber);
    flex: none;
  }
  .brand {
    position: absolute;
    display: flex;
    flex-direction: column;
    align-items: center;
    width: 240px;
  }
  .card--front .brand { left: 427px; top: 52px; }
  .card--back .brand { left: 71px; top: 76px; }
  .brand__mark {
    width: 150px;
    height: 150px;
    border-radius: 50%;
    background: var(--leaf);
  }
  .brand__name {
    margin-top: 12px;
    font-family: "Marcellus", serif;
    font-size: 34px;
    line-height: 38px;
    color: var(--forest);
    white-space: nowrap;
  }
</style>
</head>
<body>
<div class="canvas">

  <section class="card card--front" aria-label="Business card front">
    <svg class="card__shapes" viewBox="0 0 700 400" aria-hidden="true">
      <path d="M0,0 L158,0 C120,30 60,46 0,46 Z" fill="var(--amber)"/>
      <path d="M0,182 C120,135 270,150 420,255 C520,322 600,330 700,302 L700,400 L0,400 Z" fill="var(--forest)"/>
    </svg>

    <h1 class="card__name">TOBIN MARSH</h1>

    <div class="brand">
      <div class="brand__mark" role="img" aria-label="Company logo mark"></div>
      <div class="brand__name">Maple Ridge</div>
    </div>

    <div class="card__details">
      <p class="card__tagline">Lawn and Landscape<br>Maintenance Services</p>
      <div class="contact">
        <svg class="contact__icon" viewBox="0 0 24 24" aria-hidden="true">
          <path d="M6.6 10.8a15 15 0 0 0 6.6 6.6l2.2-2.2a1 1 0 0 1 1-.25 11.4 11.4 0 0 0 3.6.57 1 1 0 0 1 1 1V20a1 1 0 0 1-1 1A17 17 0 0 1 3 4a1 1 0 0 1 1-1h3.5a1 1 0 0 1 1 1c0 1.25.2 2.45.57 3.57a1 1 0 0 1-.25 1z"/>
        </svg>
        <span>555-318-7642</span>
      </div>
      <div class="contact">
        <svg class="contact__icon" viewBox="0 0 24 24" aria-hidden="true">
          <path d="M2 5h20v14H2z M2 5l10 8 10-8" fill="var(--amber)"/>
          <path d="M3 6l9 7 9-7" fill="none" stroke="var(--forest)" stroke-width="2"/>
        </svg>
        <span>service@mapleridgelandscaping.example</span>
      </div>
    </div>
  </section>

  <section class="card card--back" aria-label="Business card back">
    <svg class="card__shapes" viewBox="0 0 700 400" aria-hidden="true">
      <circle cx="606" cy="180" r="210" fill="var(--amber)"/>
      <path d="M0,354 C150,385 265,340 385,278 C505,212 600,186 700,188 L700,400 L0,400 Z" fill="var(--forest)"/>
    </svg>

    <div class="brand">
      <div class="brand__mark" role="img" aria-label="Company logo mark"></div>
      <div class="brand__name">Maple Ridge</div>
    </div>
  </section>

</div>
</body>
</html>
```